International Shipping Company requires business card designs

We are a company based in Dubai UAE with our core business being shipping and container services. Our details can be found at www.coralwakefreight.com

We are not looking for a design that necessarily involves "ships or other shipping pictures", although some reference to the business in design or colour is encouraged.

Overall design of the card must be smart and depict the company which is very professional. Fonts, colours and layout must be very contemporary in look.

Shipping

```html
<!DOCTYPE html>
<html lang="en">
<head>
<meta charset="utf-8">
<title>Coral Wake International Shipping – Business Card</title>
<link rel="stylesheet" href="https://fonts.googleapis.com/css2?family=Oswald:wght@600;700&family=Roboto+Condensed:wght@400&family=Arimo:wght@400&display=swap">
<style>
  :root {
    --canvas: #e9eced;
    --charcoal: #242b2d;
    --orange: #ec8c06;
    --steel: #8a9699;
    --tagline: #7b8587;
    --slate-tab: #718888;
    --slate-shadow: #3c4444;
    --band: #b5800b;
    --band-dark: #6b5f08;
    --ink: #0d0d0d;
    --white: #ffffff;
    --emblem: #1f35a8;
  }
  * { margin: 0; padding: 0; box-sizing: border-box; }
  html, body {
    width: 1080px; height: 1200px; overflow: hidden;
    background: var(--canvas);
  }
  .canvas { position: relative; width: 1080px; height: 1200px; }

  .card {
    position: absolute; left: 110px; width: 840px; height: 480px;
    overflow: hidden;
  }

  /* Front */
  .card--front { top: 93px; background: var(--charcoal); }
  .side-tab {
    position: absolute; top: 93px; height: 294px; background: var(--orange);
  }
  .side-tab--left { left: 0; width: 30px; border-radius: 0 8px 8px 0; }
  .side-tab--right { right: 0; width: 27px; border-radius: 8px 0 0 8px; }
  .website {
    position: absolute; left: 0; right: 0; top: 197px; text-align: center;
    font: 700 45px/1 "Oswald", sans-serif; letter-spacing: -0.5px;
    color: var(--steel);
  }
  .brand-name {
    position: absolute; left: 0; right: 0; top: 262px; text-align: center;
    font: 700 46px/1 "Oswald", sans-serif; letter-spacing: 9px;
    color: var(--orange);
  }
  .tagline {
    position: absolute; left: 0; right: 0; top: 315px; text-align: center;
    font: 400 19px/1 "Arimo", sans-serif; letter-spacing: 1.5px;
    color: var(--tagline);
  }
  .brand-dot {
    position: absolute; left: 376px; top: 362px; width: 88px; height: 88px;
    border-radius: 50%; background: var(--emblem);
  }

  /* Back */
  .card--back { top: 621px; background: var(--orange); }
  .card__arc { position: absolute; left: 0; top: 0; }
  .corner-tab {
    position: absolute; right: 0; top: 0; width: 153px; height: 74px;
    background: var(--slate-tab); border-radius: 0 0 0 14px;
    box-shadow: 0 3px 0 var(--slate-shadow);
  }
  .person-name {
    position: absolute; left: 17px; top: 182px; white-space: nowrap;
    font: 400 72px/1 "Roboto Condensed", sans-serif; letter-spacing: -1.5px;
    color: var(--ink);
    transform: scaleX(0.76); transform-origin: left top;
  }
  .person-role {
    position: absolute; left: 17px; top: 264px; white-space: nowrap;
    font: 400 40px/1 "Roboto Condensed", sans-serif;
    color: var(--ink);
    transform: scaleX(0.9); transform-origin: left top;
  }
  .contact {
    position: absolute; right: 23px; top: 216px; text-align: right;
    font: 400 25px/40px "Arimo", sans-serif; letter-spacing: 0.8px;
    font-style: normal;
    color: var(--ink);
  }
  .email-band {
    position: absolute; left: 0; bottom: 0; width: 100%; height: 56px;
    background: var(--band);
  }
  .email-band__block {
    position: absolute; left: 0; top: 0; width: 67px; height: 56px;
    background: var(--band-dark);
  }
  .email-band__text {
    position: absolute; left: 67px; right: 0; top: 0; text-align: center;
    font: 400 25px/56px "Arimo", sans-serif; letter-spacing: 0.5px;
    color: var(--white);
  }
  .email-band__label { color: var(--band-dark); }
</style>
</head>
<body>
<main class="canvas">
  <section class="card card--front">
    <div class="side-tab side-tab--left"></div>
    <div class="side-tab side-tab--right"></div>
    <p class="website">www.coralwakefreight.com</p>
    <p class="brand-name">CORAL WAKE</p>
    <p class="tagline">INTERNATIONAL SHIPPING (L.L.C.)</p>
    <div class="brand-dot"></div>
  </section>

  <section class="card card--back">
    <svg class="card__arc" width="840" height="480" viewBox="0 0 840 480" aria-hidden="true">
      <defs>
        <radialGradient id="arcShade" cx="71" cy="291" r="334" gradientUnits="userSpaceOnUse">
          <stop offset="0" stop-color="#ffffff"/>
          <stop offset="0.6" stop-color="#e4e9ea"/>
          <stop offset="0.92" stop-color="#c3ced1"/>
          <stop offset="1" stop-color="#a5b5ba"/>
        </radialGradient>
      </defs>
      <circle cx="71" cy="291" r="334" fill="url(#arcShade)"/>
    </svg>
    <div class="corner-tab"></div>
    <h1 class="person-name">Mr. Tariq Haddad</h1>
    <p class="person-role">chairman</p>
    <address class="contact">
      P.O. BOX 40562, Dubai, U.A.E.<br>
      Tel: +971 4 2870140<br>
      Fax: +971 4 2870141
    </address>
    <div class="email-band">
      <div class="email-band__block"></div>
      <p class="email-band__text"><span class="email-band__label">Email:</span> info@coralwakefreight.com</p>
    </div>
  </section>
</main>
</body>
</html>
```